Hallo,
ich bin gerade dabei, ein ebook über alternative Heilmethoden für die Frauenkrankheit Endometriose zu schreiben. Dafür brauche ich ein ausdrucksstarkes Cover. Meine Zielgruppe sind dementsprechend Frauen, die Endometriose haben. Bei Endometriose wächst Schleimhaut aus der Gebärmutter im Bauchraum, den Eierstöcken usw. Symptome sind u.a. starke Schmerzen und Kinderlosigkeit. Die Krankheit ist schulmedizinisch nicht gut behandelbar und nicht heilbar, aber es gibt zahlreiche alternative Heilmethoden, die die Symptome lindern können. Darüber soll das Buch handeln. Hier die Website zum Buch: http://www.lindenblattwissen.de/
Vielen Dank und freundliche Grüße
Katrin Wollny
Das Cover soll eine positive Stimmung rüber bringen. So wie das Bild auf der Website. Leider darf ich das Bild nur für die Website verwenden.

```html
<!DOCTYPE html>
<html lang="de">
<head>
<meta charset="utf-8">
<title>Lindenblattwissen – Buchcover</title>
<link rel="stylesheet" href="https://fonts.googleapis.com/css2?family=Dosis:wght@500&family=Permanent+Marker&family=Ubuntu:wght@400&display=swap">
<style>
  :root {
    --band-top: #e1520f;
    --band-bottom: #ef8b3c;
    --ink-dark: #4a2410;
    --ink-black: #141010;
    --white: #ffffff;
    --sun-core: #fffbe8;
    --sun-warm: #f6c77a;
    --sun-deep: #d9893a;
    --sea-dark: #7a4a2a;
  }
  html, body {
    margin: 0;
    padding: 0;
    width: 840px;
    height: 1200px;
    overflow: hidden;
    background: var(--white);
  }
  .cover {
    position: relative;
    width: 840px;
    height: 1200px;
    overflow: hidden;
    background: var(--white);
  }
  .band-top {
    position: absolute;
    left: 0; top: 0;
    width: 840px; height: 300px;
    background: var(--band-top);
  }
  .hero-photo {
    position: absolute;
    left: 0; top: 270px;
    width: 840px; height: 790px;
    background:
      radial-gradient(ellipse 260px 300px at 250px 480px, var(--sun-core) 0%, rgba(255,245,215,0.85) 35%, rgba(246,199,122,0) 100%),
      linear-gradient(180deg, #fbe7c8 0%, var(--sun-warm) 45%, var(--sun-deep) 75%, var(--sea-dark) 100%);
  }
  .edges {
    position: absolute;
    left: 0; top: 0;
    width: 840px; height: 1200px;
  }
  .band-bottom {
    position: absolute;
    left: 0; top: 1068px;
    width: 840px; height: 132px;
    background: var(--band-bottom);
  }
  .author {
    position: absolute;
    left: 77px; top: 100px;
    margin: 0;
    font-family: "Ubuntu", sans-serif;
    font-size: 33px;
    font-weight: 400;
    color: var(--ink-dark);
    letter-spacing: 0.2px;
  }
  .title {
    position: absolute;
    left: 77px; top: 150px;
    margin: 0;
    white-space: nowrap;
    line-height: 1;
  }
  .title-main {
    font-family: "Dosis", sans-serif;
    font-weight: 500;
    font-size: 66px;
    color: var(--white);
    letter-spacing: 1px;
    vertical-align: baseline;
  }
  .title-accent {
    font-family: "Permanent Marker", cursive;
    font-size: 92px;
    color: var(--ink-black);
    margin-left: 4px;
    position: relative;
    top: -12px;
    display: inline-block;
    transform: rotate(-3deg);
  }
  .tagline {
    position: absolute;
    left: 0; top: 1092px;
    width: 840px;
    margin: 0;
    text-align: center;
    font-family: "Ubuntu", sans-serif;
    font-size: 33px;
    color: var(--white);
    word-spacing: 2px;
  }
  .tagline .dot { margin: 0 14px; }
</style>
</head>
<body>
<main class="cover">
  <div class="band-top"></div>
  <div class="hero-photo" role="img" aria-label="Foto: junge Frauen springen fröhlich im Gegenlicht der Abendsonne am Strand"></div>
  <svg class="edges" viewBox="0 0 840 1200" aria-hidden="true">
    <polygon points="0,292 840,276 840,266 0,280" fill="var(--white)" opacity="0.95"/>
    <polygon points="0,298 840,284 840,276 0,292" fill="var(--white)"/>
    <polygon points="0,1046 840,1038 840,1068 0,1068" fill="var(--white)"/>
  </svg>
  <div class="band-bottom"></div>

  <p class="author">Katrin Wollny</p>
  <h1 class="title"><span class="title-main">LINDENBLATT</span><span class="title-accent">Wissen</span></h1>
  <p class="tagline">verstehen<span class="dot">•</span>lindern<span class="dot">•</span>alternativ heilen</p>
</main>
</body>
</html>
```